Heater product information sheets

I need the two product information sheets organized and laid out in a clean, easy to read attractive manner. These sheets are to advertise propane heaters for outdoor use and for wholesale to propane distributors, restaurants and homeowners that need to have propane heat as the winter ends and spring begins. They will be used for chilly evenings when people want to be outside eating, drinking and being social.
Updates

Low design quality

Target Market(s)

Restaurants, hospitality industry, special events, party rental companies, home owners with backyards

Font styles to use
Sans Serif

Requirements
Must have
• My logo in the document instead of r. Kolby and company
Nice to have
• I would like to see Fire illustrated coming up the heaters and on the round glass, show it up the middle of the glass tube propane heater.

```html
<!DOCTYPE html>
<html lang="en">
<head>
<meta charset="utf-8">
<title>Glass Tube Propane Heaters</title>
<link rel="stylesheet" href="https://fonts.googleapis.com/css2?family=Baloo+2:wght@600;700;800&family=Mada:wght@400;500&display=swap">
<style>
  :root {
    --paper: #f2f2f2;
    --coral: #d15a57;
    --slate: #434a5a;
    --gold: #e3b46a;
    --sand: #ebd2ab;
    --teal: #5e9b9b;
    --ink: #2f3237;
    --hairline: #e6c99a;
  }
  * { margin: 0; padding: 0; box-sizing: border-box; }
  html, body { width: 848px; height: 1200px; overflow: hidden; background: var(--paper); }
  .sheet {
    position: relative; width: 848px; height: 1200px; overflow: hidden;
    background: var(--paper); color: var(--ink);
    font-family: "Mada", sans-serif;
  }
  .decor { position: absolute; inset: 0; }
  .title { position: absolute; left: 119px; top: 76px; font-family: "Baloo 2", sans-serif; line-height: 1; }
  .title-main { display: block; font-size: 64px; font-weight: 800; color: var(--coral); letter-spacing: -1.6px; }
  .title-sub { display: block; font-size: 40px; font-weight: 700; color: var(--slate); margin-top: 4px; letter-spacing: -0.6px; }
  .product-photo {
    position: absolute; left: 104px; top: 254px; width: 190px; height: 462px;
    border-radius: 18px;
    background:
      radial-gradient(ellipse 60% 40% at 50% 35%, rgba(250,200,110,0.55), rgba(250,200,110,0) 70%),
      linear-gradient(180deg, #f3d9a6 0%, #f1b95c 20%, #eaa544 52%, #8a6a3a 62%, #2a2a2a 72%, #1a1a1a 100%);
  }
  .section-heading {
    position: absolute; left: 339px; font-family: "Baloo 2", sans-serif;
    font-size: 28px; font-weight: 800; color: var(--coral); line-height: 1; letter-spacing: -0.3px;
  }
  .heading-specs { top: 247px; }
  .heading-details { top: 409px; }
  .spec { position: absolute; top: 296px; width: 130px; margin-left: -65px; text-align: center; }
  .spec svg { width: 38px; height: 38px; display: block; margin: 0 auto 9px; }
  .spec p { font-size: 14px; line-height: 17px; }
  .details { position: absolute; left: 370px; top: 464px; width: 400px; list-style: none; }
  .details li { position: relative; padding-left: 22px; font-size: 21px; line-height: 23px; margin-bottom: 9.8px; }
  .details li::before {
    content: ""; position: absolute; left: 0; top: 8px; width: 10px; height: 10px;
    border-radius: 50%; background: var(--gold);
  }
  .audience { position: absolute; top: 748px; width: 100px; margin-left: -50px; text-align: center; }
  .audience svg { width: 56px; height: 54px; display: block; margin: 0 auto 22px; }
  .audience p { font-size: 11.5px; line-height: 13.6px; font-weight: 500; text-transform: uppercase; }
  .contact { position: absolute; left: 72px; top: 896px; }
  .contact-heading { font-family: "Baloo 2", sans-serif; font-size: 29px; font-weight: 800; color: var(--coral); line-height: 1.1; letter-spacing: -0.3px; }
  .company { display: flex; align-items: center; font-size: 21px; margin-top: 4px; }
  .company-mark { width: 14px; height: 14px; border-radius: 50%; background: var(--coral); margin-right: 8px; }
  .contact-row { display: flex; align-items: center; margin-top: 10px; font-size: 22px; }
  .contact-item { display: flex; align-items: center; }
  .contact-item + .contact-item { margin-left: 42px; }
  .badge { width: 25px; height: 25px; border-radius: 50%; background: var(--teal); display: inline-flex; align-items: center; justify-content: center; margin-right: 12px; }
  .badge svg { width: 14px; height: 14px; }
</style>
</head>
<body>
<main class="sheet">
  <svg class="decor" width="848" height="1200" viewBox="0 0 848 1200" aria-hidden="true">
    <circle cx="145" cy="183" r="129" fill="var(--gold)"/>
    <circle cx="-42" cy="577" r="118" fill="var(--sand)"/>
    <circle cx="848" cy="1210" r="130" fill="var(--sand)"/>
    <circle cx="656" cy="643" r="324" fill="none" stroke="var(--hairline)" stroke-width="0.8"/>
    <circle cx="-150" cy="1260" r="405" fill="none" stroke="var(--hairline)" stroke-width="0.8"/>
  </svg>

  <h1 class="title">
    <span class="title-main">Glass Tube</span>
    <span class="title-sub">Propane Heaters</span>
  </h1>

  <div class="product-photo" role="img" aria-label="Product photo: glass tube patio heater with flame rising up the centre of the glass tube, reflector top and black base"></div>

  <h2 class="section-heading heading-specs">SPECIFICATIONS</h2>

  <div class="spec" style="left:368px">
    <svg viewBox="0 0 40 40" fill="none" stroke="var(--teal)" stroke-width="1.6" stroke-linecap="round" stroke-linejoin="round">
      <path d="M22 6 L14 22 H20 L17 34 L27 17 H21 Z"/>
      <path d="M20 1v3M6 20H3M37 20h-3M9 9l2 2M31 9l-2 2M9 31l2-2M31 31l-2-2"/>
    </svg>
    <p>Powerful<br>48,000 BTU</p>
  </div>
  <div class="spec" style="left:482px">
    <svg viewBox="0 0 40 40" fill="none" stroke="var(--teal)" stroke-width="1.6" stroke-linejoin="round">
      <path d="M4 6h32v6c0 10-4 20-16 20S4 22 4 12z"/>
      <path d="M9 10v6c0 3 3 3 3 0v-2c0 3 4 3 4 0M22 12c0 3 4 3 4 0v3c0 3 3 3 3 0v-5"/>
      <path d="M8 32v4h24v-4"/>
    </svg>
    <p>Black Powder<br>Coated Finish</p>
  </div>
  <div class="spec" style="left:610px">
    <svg viewBox="0 0 40 40" fill="none" stroke="var(--teal)" stroke-width="1.6" stroke-linejoin="round">
      <rect x="16" y="2" width="8" height="4"/>
      <path d="M17 6v4M23 6v4"/>
      <rect x="11" y="10" width="18" height="28" rx="4"/>
      <path d="M11 20h18M11 28h18M9 20v8"/>
    </svg>
    <p>Uses 20 lbs.<br>Propane Tank</p>
  </div>
  <div class="spec" style="left:739px">
    <svg viewBox="0 0 40 40" fill="none" stroke="var(--teal)" stroke-width="1.6" stroke-linejoin="round">
      <rect x="9" y="3" width="24" height="30" rx="2"/>
      <path d="M4 33h24v4H6a2 2 0 0 1-2-2z"/>
      <circle cx="21" cy="13" r="4"/>
      <path d="M14 22h14M14 26h10"/>
    </svg>
    <p>CE, GS, AGA, CSA,<br>with ETL certificate<br>and ROHS approved.</p>
  </div>

  <h2 class="section-heading heading-details">ADDITIONAL DETAILS</h2>

  <ul class="details">
    <li>Commercial Quality</li>
    <li>For Outdoor Use Only</li>
    <li style="word-spacing:14px">Conforms to ANSI STD Z83.26-2014</li>
    <li>Certified to CSA STD 2.37-2014 Gas- fired outdoor infrared patio heaters</li>
    <li>Safety Auto Shut Off Switch</li>
    <li>Thermostatic Control</li>
    <li>Base Diameter 17” - Anti-Tip Design</li>
    <li>Standard Wheels - Tilt &amp; Move</li>
    <li>Run time: 8-10 hours with standard 20 lbs. Propane tank</li>
    <li>96” Tall</li>
    <li>Heating Area: 200 sq. ft</li>
  </ul>

  <div class="audience" style="left:77px">
    <svg viewBox="0 0 58 56" fill="none" stroke="var(--teal)" stroke-width="1.6" stroke-linejoin="round">
      <path d="M2 10 Q28 14 54 2M4 10l4 8 4-7 4 7 4-7 4 6 4-7 4 5 4-7 4 5 4-7 4 4 4-7"/>
      <path d="M14 30 Q34 30 56 26M16 30l4 7 4-6 4 6 4-6 4 5 4-6 4 5 4-6"/>
      <path d="M2 42 Q24 46 46 38M4 42l4 8 4-7 4 7 4-7 4 6 4-7 4 5 4-7"/>
    </svg>
    <p>Rentals for<br>live events</p>
  </div>
  <div class="audience" style="left:187px">
    <svg viewBox="0 0 58 56" fill="none" stroke="var(--teal)" stroke-width="1.6" stroke-linejoin="round">
      <circle cx="29" cy="4" r="2.5"/>
      <path d="M8 30a21 21 0 0 1 42 0z"/>
      <path d="M4 30h50v4H4z"/>
      <path d="M12 38h22l12-6M4 40h8v14H4z"/>
      <path d="M12 50h22l16-10"/>
    </svg>
    <p>Rentals for<br>restaurants &amp;<br>catering halls</p>
  </div>
  <div class="audience" style="left:295px">
    <svg viewBox="0 0 58 56" fill="none" stroke="var(--teal)" stroke-width="1.6" stroke-linejoin="round">
      <path d="M4 26 L29 6 L54 26"/>
      <path d="M40 14V3h6v16"/>
      <path d="M10 22v30h38V22"/>
      <rect x="16" y="32" width="12" height="12"/>
      <path d="M22 32v12M16 38h12"/>
      <path d="M34 52V36h8v16M4 52h50"/>
    </svg>
    <p>Purchase for<br>your home or<br>business</p>
  </div>

  <section class="contact">
    <h2 class="contact-heading">To Rent or Purchase:</h2>
    <p class="company"><span class="company-mark" aria-hidden="true"></span>R. Kolby and Company</p>
    <div class="contact-row">
      <span class="contact-item">
        <span class="badge"><svg viewBox="0 0 14 14" fill="#f2f2f2"><path d="M3 1l2 3-1 1.5c.7 1.8 2 3.1 3.6 3.8L9 8l3 2-1 2.5C6 12.5 1.5 8 1.5 2.8z"/></svg></span>
        555-301-4827
      </span>
      <span class="contact-item">
        <span class="badge"><svg viewBox="0 0 14 14" fill="none" stroke="#f2f2f2" stroke-width="1.2"><rect x="1.5" y="3" width="11" height="8"/><path d="M1.5 3l5.5 4.5L12.5 3"/></svg></span>
        hello@kolbyevents.com
      </span>
    </div>
    <div class="contact-row">
      <span class="contact-item">
        <span class="badge"><svg viewBox="0 0 14 14" fill="none" stroke="#f2f2f2" stroke-width="1.2"><path d="M7 13s-4-4.5-4-7.5a4 4 0 0 1 8 0C11 8.5 7 13 7 13z"/><circle cx="7" cy="5.5" r="1.5"/></svg></span>
        42 Foundry Lane Millbrook, NJ 07000
      </span>
    </div>
  </section>
</main>
</body>
</html>
```